Corvelle Strategies business card

I need a business card for my new strategic consulting LLC, Corvelle Strategies. We specialize in helping people who care about broadband technology and telecommunications policy, and we're based in Washington DC. I'm looking for a card that says smart, credible, future-facing and signals a high level of expertise. It's DC, so there's clearly a limit to how crazy we can go with this card, but I am looking for a design that reflects a company that is comfortable with technology, policy, and having a little bit fun. I'm uploading my logo below, and I'd like to have it be part of the card design in some fashion.
Target Market(s)
Telecommunications and technology policy professionals
Industry/Entity Type
Technology policy
Contact Information for Business Card
Name of business, my name (Glen Mosswater), email (glen@corvellestrategies-example.com) , phone number (202-555-0148)phone number

```html
<!DOCTYPE html>
<html lang="en">
<head>
<meta charset="utf-8">
<title>Corvelle Strategies – Business Card</title>
<link rel="stylesheet" href="https://fonts.googleapis.com/css2?family=Montserrat:wght@400;500;700;800&display=swap">
<style>
  :root {
    --brand-blue: #2a56a0;
    --sun-gold: #f9b23b;
    --paper: #ffffff;
    --backdrop: #e4e5e8;
    --shadow: rgba(20, 25, 40, 0.22);
  }
  * { box-sizing: border-box; margin: 0; padding: 0; }
  html, body { width: 1200px; height: 875px; overflow: hidden; }
  body {
    background: var(--backdrop);
    font-family: "Montserrat", Arial, sans-serif;
    position: relative;
  }
  .card {
    position: absolute;
    width: 540px;
    height: 310px;
    border-radius: 22px;
    overflow: hidden;
    box-shadow: 0 14px 34px var(--shadow);
  }

  /* Back side */
  .card-back {
    left: 70px;
    top: 110px;
    background: var(--brand-blue);
    display: flex;
    align-items: center;
    justify-content: center;
  }
  .wordmark {
    display: flex;
    align-items: center;
    gap: 16px;
    font-weight: 800;
    line-height: 1;
  }
  .wordmark-name { display: block; }
  .wordmark-dot {
    border-radius: 50%;
    background: var(--sun-gold);
    flex: none;
  }
  .card-back .wordmark { color: var(--paper); }
  .card-back .wordmark-name { font-size: 44px; }
  .card-back .wordmark-sub { display: block; font-size: 20px; letter-spacing: 8px; margin-top: 8px; }
  .card-back .wordmark-dot { width: 34px; height: 34px; }

  /* Front side */
  .card-front {
    left: 590px;
    top: 450px;
    background: var(--paper);
  }
  .card-front .band {
    position: absolute;
    inset: 0;
    width: 100%;
    height: 100%;
  }
  .card-front .wordmark {
    position: absolute;
    left: 34px;
    top: 40px;
    color: var(--brand-blue);
    gap: 10px;
  }
  .card-front .wordmark-name { font-size: 26px; }
  .card-front .wordmark-sub { display: block; font-size: 11px; letter-spacing: 4.5px; margin-top: 5px; }
  .card-front .wordmark-dot { width: 18px; height: 18px; }

  .contact {
    position: absolute;
    left: 36px;
    top: 196px;
    color: var(--paper);
  }
  .contact-name {
    color: var(--sun-gold);
    font-weight: 700;
    font-size: 17px;
    letter-spacing: 0.5px;
    text-transform: uppercase;
  }
  .contact-title { font-size: 12px; font-weight: 400; margin-top: 2px; }
  .contact-list { list-style: none; margin-top: 12px; }
  .contact-list li {
    display: flex;
    align-items: center;
    gap: 8px;
    font-size: 11.5px;
    margin-top: 5px;
  }
  .icon { width: 12px; height: 12px; flex: none; }
  .website {
    position: absolute;
    right: 26px;
    bottom: 26px;
    display: flex;
    align-items: center;
    gap: 8px;
    color: var(--paper);
    font-size: 11.5px;
  }
</style>
</head>
<body>

  <section class="card card-back" aria-label="Card back">
    <div class="wordmark">
      <span>
        <span class="wordmark-name">Corvelle</span>
        <span class="wordmark-sub">STRATEGIES</span>
      </span>
      <span class="wordmark-dot"></span>
    </div>
  </section>

  <section class="card card-front" aria-label="Card front">
    <svg class="band" viewBox="0 0 540 310" preserveAspectRatio="none" aria-hidden="true">
      <line x1="0" y1="172" x2="540" y2="18" stroke="#2a56a0" stroke-width="3"/>
      <polygon points="0,186 540,32 540,310 0,310" fill="#2a56a0"/>
    </svg>

    <div class="wordmark">
      <span>
        <span class="wordmark-name">Corvelle</span>
        <span class="wordmark-sub">STRATEGIES</span>
      </span>
      <span class="wordmark-dot"></span>
    </div>

    <div class="contact">
      <p class="contact-name">Glen Mosswater</p>
      <p class="contact-title">CEO/Founder</p>
      <ul class="contact-list">
        <li>
          <svg class="icon" viewBox="0 0 24 24" aria-hidden="true"><path fill="#f9b23b" d="M6.6 10.8a15.1 15.1 0 0 0 6.6 6.6l2.2-2.2a1 1 0 0 1 1-.25 11.4 11.4 0 0 0 3.6.57 1 1 0 0 1 1 1V20a1 1 0 0 1-1 1A17 17 0 0 1 3 4a1 1 0 0 1 1-1h3.5a1 1 0 0 1 1 1c0 1.25.2 2.45.57 3.57a1 1 0 0 1-.25 1z"/></svg>
          <span>202-555-0148</span>
        </li>
        <li>
          <svg class="icon" viewBox="0 0 24 24" aria-hidden="true"><path fill="#f9b23b" d="M3 5h18a1 1 0 0 1 1 1v12a1 1 0 0 1-1 1H3a1 1 0 0 1-1-1V6a1 1 0 0 1 1-1zm1 2.2V17h16V7.2l-8 5.3z"/></svg>
          <span>glen@corvellestrategies-example.com</span>
        </li>
      </ul>
    </div>

    <div class="website">
      <svg class="icon" viewBox="0 0 24 24" aria-hidden="true"><circle cx="12" cy="12" r="9" fill="none" stroke="#f9b23b" stroke-width="2.4"/><path d="M3 12h18M12 3c3 3.2 3 14.8 0 18M12 3c-3 3.2-3 14.8 0 18" fill="none" stroke="#f9b23b" stroke-width="1.8"/></svg>
      <span>corvellestrategies-example.com</span>
    </div>
  </section>

</body>
</html>
```